Menu Design marlowe

I need to create a take out menu for my restaurant something nice with some pictures. clean and simple with the colors of my reatsurant. which are orange and black. mostly black.

its fairly simple it has to be 4 pages front cover, inside front menu then 2nd page front and back with menu then 3rd page back front menu, back 3rd sushi menu with specials. final page 4th page, back map with adress and opening hours. and back cover final.

simple elegant and class. black and orange i will send logo and menu as well and pictures.

i am a high end bistro that serves gourmet pizza and pasta. we also have a sushi bar.
the menu will be 6 inches width by 9 inches

the menu that i sent is a pdf file. had an error with word please change font and make a new word dosument.

thank you

Industry/Entity Type

Restaurant

Requirements
Must have
• the colors which are black and orange. mostly black.

```html
<!DOCTYPE html>
<html lang="fr">
<head>
<meta charset="utf-8">
<title>marlowe – Menu</title>
<link rel="stylesheet" href="https://fonts.googleapis.com/css2?family=Patrick+Hand+SC&family=Open+Sans:ital,wght@1,700&display=swap">
<style>
  :root {
    --page-black: #050505;
    --swirl-tone: #2a1a0e;
    --swirl-orange: #3a220c;
    --gutter-light: #8a8a8a;
    --gutter-dark: #3c3c3c;
    --ink: #f4f4f4;
    --map-frame: #ffffff;
    --map-light: #eeeae0;
    --map-mid: #e3dccb;
    --icon-bg: #1c1c1c;
  }
  * { margin: 0; padding: 0; box-sizing: border-box; }
  html, body { width: 1200px; height: 900px; overflow: hidden; background: var(--page-black); }
  .spread { position: relative; width: 1200px; height: 900px; }

  .page { position: absolute; top: 0; height: 900px; overflow: hidden; background: var(--page-black); }
  .page--menu { left: 0; width: 590px; }
  .page--contact { left: 610px; width: 590px; }
  .page__texture {
    position: absolute; inset: 0;
    background:
      radial-gradient(ellipse 260px 180px at 80px 120px, var(--swirl-tone), transparent 70%),
      radial-gradient(ellipse 220px 200px at 140px 700px, var(--swirl-orange), transparent 70%),
      radial-gradient(ellipse 240px 200px at 470px 620px, var(--swirl-tone), transparent 70%);
    opacity: .55;
  }
  .gutter {
    position: absolute; left: 590px; top: 0; width: 20px; height: 900px;
    background: linear-gradient(90deg, var(--gutter-dark), var(--gutter-light) 45%, var(--gutter-dark));
  }

  /* menu */
  .menu { position: absolute; left: 0; top: 0; width: 590px; font-family: "Patrick Hand SC", cursive; color: var(--ink); font-size: 11.5px; text-transform: uppercase; letter-spacing: .1px; }
  .menu__title { position: absolute; top: 47px; left: 0; width: 628px; text-align: center; font-size: 11.5px; font-weight: 400; }
  .menu__list { position: absolute; top: 88px; left: 0; width: 590px; list-style: none; }
  .menu__row { position: relative; height: 19.7px; line-height: 19.7px; padding-left: 102px; white-space: nowrap; }
  .menu__row--heading, .menu__row--note { padding-left: 0; text-align: center; width: 648px; }
  .menu__row--heading { width: 652px; }
  .menu__row--note-sauce { width: 652px; }
  .menu__price { position: absolute; left: 463px; top: 0; }
  .menu__price--tilapia { left: 436px; }
  .menu__price--lasagna { left: 431px; }

  /* contact */
  .map {
    position: absolute; left: 48px; top: 62px; width: 496px; height: 355px;
    border: 2px solid var(--map-frame);
    background: linear-gradient(135deg, var(--map-light), var(--map-mid));
  }
  .address {
    position: absolute; left: 0; top: 484px; width: 590px; text-align: center;
    font-family: "Open Sans", sans-serif; font-style: italic; font-weight: 700;
    color: var(--ink); font-size: 29px; line-height: 41.5px; letter-spacing: 1px;
  }
  .address span { display: block; }
  .phone { position: absolute; left: 135px; top: 717px; display: flex; align-items: center; gap: 20px; }
  .phone__icon { width: 73px; height: 70px; border-radius: 10px; background: var(--icon-bg); display: flex; align-items: center; justify-content: center; }
  .phone__number { font-family: "Open Sans", sans-serif; font-style: italic; font-weight: 700; font-size: 29px; color: var(--ink); letter-spacing: 2.2px; }
</style>
</head>
<body>
<main class="spread">
  <section class="page page--menu">
    <div class="page__texture" role="img" aria-label="Faint orange swirl ornament on black"></div>
    <div class="menu">
      <h2 class="menu__title">Poisson /Fish</h2>
      <ul class="menu__list">
        <li class="menu__row menu__row--note">Servi avec 2 choix de salade verte, legumes du jour, riz ou frites</li>
        <li class="menu__row menu__row--note">Served with a choice of green salade, vegetables, rice or fries</li>
        <li class="menu__row">Fish n chips<span class="menu__price">$19.50</span></li>
        <li class="menu__row">Saumon grille / grilled salmon<span class="menu__price">$21.95</span></li>
        <li class="menu__row">Tilapia au four<span class="menu__price menu__price--tilapia">$19.50</span></li>
        <li class="menu__row">Oven roasted tilapia</li>
        <li class="menu__row">Steak de thon style tataki / tataki style tuna steak<span class="menu__price">$25.95</span></li>
        <li class="menu__row">Crevettes sautees a l'ail (10)<span class="menu__price">$21.95</span></li>
        <li class="menu__row menu__row--heading">A cotes / sides</li>
        <li class="menu__row">Frites / french fries<span class="menu__price">$3.50</span></li>
        <li class="menu__row">Frites epicees / spicy french fries<span class="menu__price">$4.50</span></li>
        <li class="menu__row">Sweet potatoes fries / frite pomme de terre douce<span class="menu__price">$4.95</span></li>
        <li class="menu__row">Riz / rice<span class="menu__price">$3.00</span></li>
        <li class="menu__row">Legumes grilles de saison / seasonal grilled vegetables<span class="menu__price">$5.95</span></li>
        <li class="menu__row">Patates / potatoes<span class="menu__price">$3.50</span></li>
        <li class="menu__row">Salade verte /green salad<span class="menu__price">$3.25</span></li>
        <li class="menu__row">Thon &nbsp; / &nbsp; tuna<span class="menu__price">$3.00</span></li>
        <li class="menu__row">Oeuf dur / boiled egg<span class="menu__price">$3.00</span></li>
        <li class="menu__row menu__row--heading">Pates &nbsp;/ pasta</li>
        <li class="menu__row menu__row--note menu__row--note-sauce">Sauces: tomate -arabiata - alfredo -</li>
        <li class="menu__row menu__row--note menu__row--note-sauce">Pesto &amp; ail -bella rosa - marsala champignon</li>
        <li class="menu__row">Spaghetti<span class="menu__price">$14.95</span></li>
        <li class="menu__row">Penne<span class="menu__price">$14.95</span></li>
        <li class="menu__row">Fettuccini<span class="menu__price">$14.95</span></li>
        <li class="menu__row">Ravioli aux champignons sauvages<span class="menu__price">$17.50</span></li>
        <li class="menu__row">Wild mushroom ravioli</li>
        <li class="menu__row">Ravioli a la ricotta &nbsp;epinards<span class="menu__price">$17.50</span></li>
        <li class="menu__row">Ravioli &nbsp;with &nbsp;ricotta &amp; spinach</li>
        <li class="menu__row">Ravioli a la pomme de terre douce<span class="menu__price">$17.50</span></li>
        <li class="menu__row">Sweet potatoes ravioli</li>
        <li class="menu__row">Lasagne vegetarienne<span class="menu__price menu__price--lasagna">$14.95</span></li>
        <li class="menu__row">Veggie lasagna</li>
        <li class="menu__row">Sur &nbsp;demande</li>
      </ul>
    </div>
  </section>

  <div class="gutter"></div>

  <section class="page page--contact">
    <div class="page__texture" role="img" aria-label="Faint orange swirl ornament on black"></div>
    <div class="map" role="img" aria-label="Street map showing the restaurant location"></div>
    <address class="address">
      <span>2180, ch Bellweather</span>
      <span>Montréal</span>
      <span>QC H2Z 4K8</span>
      <span>Canada</span>
    </address>
    <div class="phone">
      <div class="phone__icon">
        <svg width="50" height="42" viewBox="0 0 50 42" aria-hidden="true">
          <path d="M4 14 C4 4 46 4 46 14 L46 18 L36 18 L36 13 L14 13 L14 18 L4 18 Z" fill="#fff"/>
          <path d="M16 16 L34 16 L42 30 L42 38 L8 38 L8 30 Z" fill="#fff"/>
          <g fill="#1c1c1c">
            <rect x="18" y="22" width="3" height="3"/><rect x="23.5" y="22" width="3" height="3"/><rect x="29" y="22" width="3" height="3"/>
            <rect x="17" y="27" width="3" height="3"/><rect x="23.5" y="27" width="3" height="3"/><rect x="30" y="27" width="3" height="3"/>
            <rect x="16" y="32" width="3" height="3"/><rect x="23.5" y="32" width="3" height="3"/><rect x="31" y="32" width="3" height="3"/>
          </g>
        </svg>
      </div>
      <span class="phone__number">(514) 555 0142</span>
    </div>
  </section>
</main>
</body>
</html>
```